Business Card/Email Signature design

We need an new business card design for our business as well as an animated email signature design.<br/>Business Card:<br/>The business card designs need to have the following information for each director:<br/>Leon Bramwell<br/>Managing Director<br/>leon@talvoraworks.com.au<br/>0498617340<br/>www.talvoraworks.com.au<br/><br/>and<br/><br/>Priscilla Venton<br/>Director<br/>priscilla@talvoraworks.com.au<br/>0467302958<br/>www.talvoraworks.com.au<br/><br/>I will upload the Talvora. Works logo designs to be used for the design. Our colours are black and white. I would like to see the designs in both coloured backgrounds.<br/><br/>For the email signature we need the same information. I also need to add a logo of our association BLPX of which i will add the logo as well. This BLPX logo does not need to be used for the business card unless it works with the design.<br/>For the animation part of the logo our company is called Talvora. Works - We have a number of divisions called Talvora. Construct, Talvora. Property, Talvora. Sales, Talvora. Executive Support, Talvora. Private PA, Talvora. Talent and Talvora. Coaching<br/>I would like for the email Signature to be designed so that the Talvora. stays still but the words Construct, Property, Sales, Executive Support, Private PA, Talent and Coaching rotate through to capture attention and tell the story of what we do.<br/><br/>Any questions please don't hesitate to message me.

Industry/Entity Type

Recruiter

Contact Information for Business Card

Leon Bramwell
Managing Director
leon@talvoraworks.com.au
0498617340
www.talvoraworks.com.au

Priscilla Venton
Director
priscilla@talvoraworks.com.au
0467302958
www.talvoraworks.com.au

Font styles to use
Serif

Colors

Designer to choose colors to be used in the design.

Requirements
Must have
• The animation for the email signature as described
Should not have
• Any changes to my logo. Any colour other that black or white

```html
<!DOCTYPE html>
<html lang="en">
<head>
<meta charset="utf-8">
<title>Talvora. Works – Business Card</title>
<link rel="stylesheet" href="https://fonts.googleapis.com/css2?family=Roboto:wght@400;500;700&display=swap">
<style>
  :root {
    --backdrop: #e6e6e6;
    --card-light: #ffffff;
    --card-dark: #262626;
    --ink: #111111;
    --ink-soft: #3a3a3a;
    --rule: #9a9a9a;
    --foil: #8c8c8c;
  }
  * { box-sizing: border-box; margin: 0; padding: 0; }
  html, body {
    width: 1200px;
    height: 801px;
    overflow: hidden;
    background: var(--backdrop);
    font-family: "Roboto", Arial, sans-serif;
  }
  .canvas {
    position: relative;
    width: 1200px;
    height: 801px;
  }
  .card {
    position: absolute;
    top: 250px;
    width: 520px;
    height: 298px;
    box-shadow: 0 6px 18px rgba(0,0,0,0.12);
  }
  .card--front { left: 50px; background: var(--card-light); color: var(--ink); }
  .card--back { left: 630px; background: var(--card-dark); }

  /* Front card */
  .brand {
    position: absolute;
    display: flex;
    align-items: center;
    gap: 12px;
    font-weight: 500;
    white-space: nowrap;
  }
  .card--front .brand {
    left: 36px;
    top: 128px;
    font-size: 20px;
    color: var(--ink);
  }
  .brand__square {
    width: 34px;
    height: 34px;
    border: 1.5px solid currentColor;
  }
  .divider {
    position: absolute;
    left: 250px;
    top: 74px;
    width: 1px;
    height: 150px;
    background: var(--rule);
  }
  .contact {
    position: absolute;
    left: 284px;
    top: 78px;
  }
  .contact__name {
    font-size: 19px;
    font-weight: 700;
    line-height: 1.1;
  }
  .contact__role {
    font-size: 13px;
    color: var(--ink-soft);
    margin-bottom: 24px;
  }
  .contact__list { list-style: none; }
  .contact__item {
    display: flex;
    align-items: center;
    gap: 9px;
    font-size: 13px;
    line-height: 20px;
    color: var(--ink-soft);
  }
  .contact__icon { width: 11px; height: 11px; flex: none; }

  /* Back card */
  .card--back .brand {
    left: 50%;
    top: 50%;
    transform: translate(-50%, -50%);
    font-size: 30px;
    gap: 18px;
    color: var(--foil);
  }
  .card--back .brand__square { width: 54px; height: 54px; }
</style>
</head>
<body>
<main class="canvas">
  <section class="card card--front" aria-label="Business card front">
    <div class="brand"><span class="brand__square"></span><span class="brand__name">Talvora. Works</span></div>
    <div class="divider"></div>
    <div class="contact">
      <p class="contact__name">Leon Bramwell</p>
      <p class="contact__role">Managing Director</p>
      <ul class="contact__list">
        <li class="contact__item">
          <svg class="contact__icon" viewBox="0 0 12 12"><path d="M3 1 L4.5 3.5 L3.4 4.6 C4 6 6 8 7.4 8.6 L8.5 7.5 L11 9 L9.8 11 C5 11 1 7 1 2.2 Z" fill="currentColor"/></svg>
          <span>0498617340</span>
        </li>
        <li class="contact__item">
          <svg class="contact__icon" viewBox="0 0 12 12"><rect x="0.75" y="2.25" width="10.5" height="7.5" fill="none" stroke="currentColor" stroke-width="1.2"/><path d="M1 2.6 L6 6.6 L11 2.6" fill="none" stroke="currentColor" stroke-width="1.2"/></svg>
          <span>leon@talvoraworks.com.au</span>
        </li>
        <li class="contact__item">
          <svg class="contact__icon" viewBox="0 0 12 12"><circle cx="6" cy="6" r="5.5" fill="currentColor"/><path d="M0.5 6 H11.5 M6 0.5 V11.5 M1.5 3.5 H10.5 M1.5 8.5 H10.5" stroke="#fff" stroke-width="0.7"/></svg>
          <span>www.talvoraworks.com.au</span>
        </li>
      </ul>
    </div>
  </section>

  <section class="card card--back" aria-label="Business card back">
    <div class="brand"><span class="brand__square"></span><span class="brand__name">Talvora. Works</span></div>
  </section>
</main>
</body>
</html>
```